Moden - Mexicali - Flower Shop

brisapetals is looking for a cool web design that has a airy, clean, mexicali feel to it.

See attached images and links for idea of what we mean with the above.

please no templates.
Updates

Target Market(s)

Local flower shop in San Diego, California

Industry/Entity Type

Shop

Requirements
Must have
• see. brisapetals.quillcart.example - I did the site and logo...I love the logo - hate the site.

Going for this feel: http://www.plumnotebook.example/tablecraft/archives/verandos.php

I also attached another site I liked- I just feel like it may be to busy.

```html
<!DOCTYPE html>
<html lang="en">
<head>
<meta charset="utf-8">
<title>Brisa Petals — Farm to Home Flowers</title>
<link rel="stylesheet" href="https://fonts.googleapis.com/css2?family=Open+Sans:wght@400;600&family=Kaushan+Script&display=swap">
<style>
  :root {
    --page-dark: #111;
    --page-mid: #3a3a3a;
    --white: #ffffff;
    --ink: #1c1c1c;
    --muted: #555;
    --lime: #9cf724;
    --lime-deep: #8ae414;
    --sale-red: #f0212b;
    --panel-dark: #2a2a2a;
    --rule: #d4d4d4;
    --link: #2340e0;
    --footer: #dcdcdc;
    --arrow-grey: #e2e2e2;
  }
  * { box-sizing: border-box; margin: 0; padding: 0; }
  html, body { width: 1200px; height: 1000px; overflow: hidden; }
  body {
    position: relative;
    font-family: "Open Sans", Arial, sans-serif;
    color: var(--ink);
    background: radial-gradient(ellipse at center, var(--page-mid) 0%, var(--page-dark) 75%);
  }
  .abs { position: absolute; }
  .site { position: absolute; left: 95px; top: 0; width: 1010px; height: 1000px; background: var(--white); }

  /* header */
  .brand { position: absolute; left: 263px; top: 11px; display: flex; align-items: center; gap: 10px;
    font-size: 17px; letter-spacing: 5px; color: #7cc7c0; }
  .brand-dot { width: 18px; height: 18px; border-radius: 50%; border: 2px solid #7cc7c0; }
  .nav a { position: absolute; top: 14px; font-size: 12px; color: var(--ink); text-decoration: none; }
  .nav-pointer { position: absolute; left: 687px; top: 40px; width: 0; height: 0;
    border-left: 6px solid transparent; border-right: 6px solid transparent; border-top: 8px solid var(--white); z-index: 3; }

  /* hero */
  .hero { position: absolute; left: 95px; top: 42px; width: 1010px; height: 486px;
    background:
      linear-gradient(180deg, #3b2a2a 0%, #8a3a26 12%, #c2452a 20%, #5a3b2c 30%, #37462b 42%, #4b5a2c 55%, #6a4a3a 70%, #3d3b36 100%); }
  .hero-field { position: absolute; left: 0; top: 170px; width: 1010px; height: 170px;
    background: linear-gradient(90deg, rgba(150,40,40,.55), rgba(80,90,40,.3) 40%, rgba(180,40,50,.45) 65%, rgba(200,190,70,.5) 85%, rgba(120,120,60,.4)); }
  .hero-band { position: absolute; left: 0; top: 331px; width: 1010px; height: 155px; background: rgba(45,45,45,.93); }

  .product { position: absolute; left: 263px; top: 88px; width: 389px; height: 393px; background: var(--white);
    border-bottom: 5px solid var(--lime); }
  .product-title { position: absolute; left: 7px; top: 7px; font-size: 20px; }
  .arrow { position: absolute; top: 0; width: 51px; height: 38px; display: flex; align-items: center; justify-content: center; }
  .arrow.prev { left: 288px; background: var(--arrow-grey); }
  .arrow.next { left: 338px; background: var(--lime); }
  .product-photo { position: absolute; left: 0; top: 38px; width: 389px; height: 247px;
    background: radial-gradient(circle at 55% 45%, #f08a1a 0%, #e0601a 30%, #5b5a52 70%, #7a7a72 100%); }
  .product-lead { position: absolute; left: 8px; top: 289px; width: 260px; font-size: 15.5px; line-height: 19px; }
  .product-sizes { position: absolute; left: 8px; top: 339px; font-size: 11.5px; line-height: 14px; }
  .price-before { position: absolute; left: 280px; top: 313px; font-size: 13px; color: var(--muted); }
  .price-before s { color: var(--sale-red); }
  .price-now { position: absolute; left: 279px; top: 328px; font-size: 17px; }
  .price-now span { color: var(--sale-red); }
  .price-now sup { font-size: 9px; color: var(--sale-red); }
  .buy-btn { position: absolute; left: 280px; top: 350px; width: 109px; height: 38px; background: var(--lime);
    color: var(--sale-red); font-size: 16px; display: flex; align-items: center; justify-content: center; }

  .tagline { position: absolute; left: 720px; top: 126px; font-family: "Kaushan Script", cursive; font-size: 35px; color: var(--white); }
  .tagline-sub { position: absolute; left: 731px; top: 178px; font-size: 11.5px; line-height: 13px; color: var(--white); }
  .call-icon { position: absolute; left: 724px; top: 233px; width: 34px; height: 34px; border-radius: 50%; background: var(--white);
    display: flex; align-items: center; justify-content: center; }
  .call-label { position: absolute; left: 763px; top: 232px; font-size: 11px; color: var(--white); }
  .call-number { position: absolute; left: 763px; top: 245px; font-size: 19px; color: var(--white); }
  .shop-btn { position: absolute; left: 726px; top: 291px; width: 126px; height: 26px; border: 2px solid var(--white);
    color: var(--white); font-size: 13px; display: flex; align-items: center; justify-content: center; }
  .newsletter-title { position: absolute; left: 724px; top: 379px; font-size: 24px; color: var(--white); }
  .newsletter-text { position: absolute; left: 726px; top: 411px; font-size: 11.5px; line-height: 13px; color: var(--white); }
  .newsletter-field { position: absolute; left: 726px; top: 454px; width: 147px; height: 26px; background: var(--white); }
  .newsletter-go { position: absolute; left: 883px; top: 453px; width: 29px; height: 29px; border-radius: 50%; background: var(--white);
    font-size: 11px; display: flex; align-items: center; justify-content: center; }

  /* collections */
  .section-title { position: absolute; left: 262px; top: 540px; font-size: 16.5px; }
  .tile-photo { position: absolute; width: 122px; height: 122px; }
  .tile-bar { position: absolute; width: 122px; height: 24px; background: var(--lime); font-size: 11.5px;
    display: flex; align-items: center; padding-left: 7px; }
  .tile-bar svg { position: absolute; right: 9px; top: 2px; }

  /* sidebar */
  .side-head { position: absolute; left: 749px; width: 192px; height: 34px; background: var(--panel-dark); color: var(--white);
    font-size: 16.5px; display: flex; align-items: center; justify-content: center; }
  .side-text { position: absolute; left: 755px; width: 180px; font-size: 11px; line-height: 13.5px; }
  .side-text a { color: var(--link); text-decoration: none; }
  .social { position: absolute; top: 654px; width: 24px; height: 24px; border-radius: 50%; }
  .side-rule { position: absolute; left: 749px; width: 192px; height: 2px; background: var(--rule); }
  .footer { position: absolute; left: 95px; top: 955px; width: 1010px; height: 45px; background: var(--footer); }
</style>
</head>
<body>
  <div class="site"></div>

  <header>
    <div class="brand"><span>BRISA PETALS</span><span class="brand-dot"></span></div>
    <nav class="nav">
      <a style="left:687px">HOME</a>
      <a style="left:750px">SHOP</a>
      <a style="left:800px">CURATED</a>
      <a style="left:875px">ABOUT US</a>
    </nav>
  </header>

  <section class="hero" role="img" aria-label="Photograph of rows of red and yellow flower fields under a sunset sky">
    <div class="hero-field"></div>
    <div class="hero-band"></div>
  </section>
  <div class="nav-pointer"></div>

  <article class="product">
    <h2 class="product-title" style="font-weight:400">Fresh Sun Flowers</h2>
    <div class="arrow prev"><svg width="14" height="24" viewBox="0 0 14 24"><polyline points="12,2 2,12 12,22" fill="none" stroke="#8ae414" stroke-width="2"/></svg></div>
    <div class="arrow next"><svg width="14" height="24" viewBox="0 0 14 24"><polyline points="2,2 12,12 2,22" fill="none" stroke="#fff" stroke-width="2"/></svg></div>
    <div class="product-photo" role="img" aria-label="Photograph of orange sunflowers wrapped in kraft paper on weathered wood"></div>
    <p class="product-lead">Sun Flowers are a great way to brighten a day.</p>
    <p class="product-sizes">Small - 5 stems<br>Medium - 10 stems<br>Large - 15 stems - (Comes with vase included)</p>
    <p class="price-before">Before: <s>$75.00</s></p>
    <p class="price-now">NOW! <span>$50</span><sup>.00</sup></p>
    <div class="buy-btn">BUY NOW!</div>
  </article>

  <h1 class="tagline" style="font-weight:400">Farm to Home</h1>
  <p class="tagline-sub">Fresh from farms in San Diego<br>Direct to your home</p>
  <div class="call-icon">
    <svg width="20" height="16" viewBox="0 0 20 16"><path d="M1 5 Q10 -1 19 5 L17 8 L14 6 L14 4 Q10 3 6 4 L6 6 L3 8 Z" fill="#222"/><rect x="4" y="8" width="12" height="7" rx="1" fill="#222"/><circle cx="10" cy="11.5" r="2" fill="#fff"/></svg>
  </div>
  <p class="call-label">Call Us Now!</p>
  <p class="call-number">619-555-0143</p>
  <div class="shop-btn">SHOP NOW!</div>
  <h2 class="newsletter-title" style="font-weight:400">NEWSLETTER</h2>
  <p class="newsletter-text">We promise to only send you<br>good things like discounts!</p>
  <div class="newsletter-field"></div>
  <div class="newsletter-go">GO</div>

  <h2 class="section-title" style="font-weight:400">Curated Collections</h2>

  <div class="tile-photo" style="left:262px;top:582px;background:linear-gradient(160deg,#e7dde3,#c99ab5 45%,#3f6b35)" role="img" aria-label="Photograph of pink and white lilies"></div>
  <div class="tile-bar" style="left:262px;top:709px">Any Occasion<svg width="20" height="20"><circle cx="10" cy="10" r="10" fill="#fff"/><polygon points="8,6 14,10 8,14" fill="#222"/></svg></div>
  <div class="tile-photo" style="left:411px;top:582px;background:linear-gradient(160deg,#8a8682,#e9467a 45%,#c4a37f 75%,#6a7a4a)" role="img" aria-label="Photograph of pink gerberas in kraft paper"></div>
  <div class="tile-bar" style="left:411px;top:709px">Birthday<svg width="20" height="20"><circle cx="10" cy="10" r="10" fill="#fff"/><polygon points="8,6 14,10 8,14" fill="#222"/></svg></div>
  <div class="tile-photo" style="left:560px;top:582px;background:linear-gradient(160deg,#6d6a66,#f2f2ef 40%,#4f7a36 80%)" role="img" aria-label="Photograph of white calla lilies"></div>
  <div class="tile-bar" style="left:560px;top:709px">Dude<svg width="20" height="20"><circle cx="10" cy="10" r="10" fill="#fff"/><polygon points="8,6 14,10 8,14" fill="#222"/></svg></div>

  <div class="tile-photo" style="left:262px;top:757px;background:linear-gradient(160deg,#7a1218,#a81a24 50%,#6b6460)" role="img" aria-label="Photograph of red roses"></div>
  <div class="tile-bar" style="left:262px;top:887px">Love<svg width="20" height="20"><circle cx="10" cy="10" r="10" fill="#fff"/><polygon points="8,6 14,10 8,14" fill="#222"/></svg></div>
  <div class="tile-photo" style="left:415px;top:757px;height:124px;background:linear-gradient(160deg,#8a8682,#f2a52a 40%,#e8602a 60%,#c9ad8a)" role="img" aria-label="Photograph of orange and yellow lilies in kraft paper"></div>
  <div class="tile-bar" style="left:415px;top:887px">Thank you<svg width="20" height="20"><circle cx="10" cy="10" r="10" fill="#fff"/><polygon points="8,6 14,10 8,14" fill="#222"/></svg></div>
  <div class="tile-photo" style="left:560px;top:757px;height:124px;background:linear-gradient(160deg,#8a8682,#f0f0ea 40%,#c9ad8a 80%)" role="img" aria-label="Photograph of white ranunculus in kraft paper"></div>
  <div class="tile-bar" style="left:560px;top:887px">Sorry<svg width="20" height="20"><circle cx="10" cy="10" r="10" fill="#fff"/><polygon points="8,6 14,10 8,14" fill="#222"/></svg></div>

  <aside>
    <div class="side-head" style="top:544px">Meet Brisa</div>
    <p class="side-text" style="top:587px">Based in Hillcrest, San Diego - We offer farm fresh, curated, cool, and same day delivery flower bouquets.</p>
    <span class="social" style="left:755px;background:#7fb2df"></span>
    <span class="social" style="left:782px;background:#51659b"></span>
    <span class="social" style="left:809px;background:#d9504a"></span>
    <div class="side-rule" style="top:688px"></div>

    <div class="side-head" style="top:717px">Reach Brisa</div>
    <p class="side-text" style="top:759px">2210 Marisol Avenue<br>San Diego, CA 92103<br><br>Email: <a>info@brisapetals.example</a><br>Phone: 619-555-0143</p>
    <div class="side-rule" style="top:841px"></div>
  </aside>

  <footer class="footer"></footer>
</body>
</html>
```